A new website for Electrical Contractor Business

We are looking for a unique and new WordPress website design which would include 5 Pages - Home Page, Meet the Team, Our Services, Our Projects and Contact Us page.

The global theme for the website needs to be professional but simple to navigate as we cater for both business and home owner customers.

Our core business service is targeted around lighting from single room decorative to large office so the theme should incorporate this in some way.

The home page should include;
Our business logo, Contact number, Email address, small Image rotation box - Highlighting pervious projectsText box - With welcome message, chirpnet feed news reel/Customer feed back box.

I would also like to see a 2 boxes for the separate customer types we services. Business and Home Owner. each box will have a small image with a small text description with a link to the area of the services page relevant to that customer type.

Meet the team page -This will be introducing potential customers to the team so I would like it to include for each team member. Something like a small image and text area which will introduce an outline of the team members skills and abilities.

Our Services page This page will be outlining the different services on offer to the both customer types business and homeowner. Each service should have an image with text description of the service would good here.

Our projects page-Will include images of pervious projects and work we have completed along with a text area for the project description/ outliner.

Contact Us page - Should include a contact form which should include an option for the customer to quest us to call them back, also a selection box for them to inform us our how they found our details would be good.

Colour - The theme colours can be taken from the logo or feel free to impress with your own imagination.

Remember we are looking for a website that will interest our customers enough to except our services or be drawn further into the website.. So call to action links to other areas of the site/ contact page are welcome

Target Market(s)

Business - Office, warehousing and Large Store - lighting and Power
Home owner lighting and power

Coding

Coded - Design and coding required

Number of Pages Required

5+ page

Font styles to use
Serif
Sans Serif

Colors

Designer to choose colors to be used in the design.

Requirements
Must have
• Logo integrated into the website design - i.e. website colours which allow the logo to blend into the design.
Nice to have
• Custom but professional theme catering to business customers, but also show that we do provide services to home owners too.
Should not have
• Sorry am not interested in one oversized block image on rotation covering half the home page.. Images will be needed but not a single block over sized frame with not text, shape. Please use your imagination when considering this design

```html
<!DOCTYPE html>
<html lang="en">
<head>
<meta charset="utf-8">
<title>Brightwire Electrical</title>
<link href="https://fonts.googleapis.com/css2?family=Arimo:wght@400;700&family=Roboto:wght@400;500;700&display=swap" rel="stylesheet">
<style>
:root{
  --navy:#2f2e63;
  --orange:#f26522;
  --orange-soft:#f47a3e;
  --text:#555a66;
  --dark:#1f2230;
  --light:#f4f4f4;
  --white:#ffffff;
}
*{box-sizing:border-box;margin:0;padding:0}
html,body{width:1200px;height:2683px;overflow:hidden;background:var(--white)}
body{position:relative;font-family:"Arimo",Arial,sans-serif;color:var(--text)}
.abs{position:absolute}
a{color:inherit;text-decoration:none}

/* header */
.brand{left:68px;top:40px;display:flex;align-items:center;gap:14px}
.brand-dot{width:56px;height:56px;border-radius:50%;background:var(--navy)}
.brand-name{font-family:"Roboto",sans-serif;font-weight:500;font-size:28px;color:var(--navy);letter-spacing:1px}
.contact-block{top:34px}
.contact-label{font-size:13px;font-weight:700;color:var(--navy);letter-spacing:.3px}
.contact-value{font-size:13px;font-weight:700;color:var(--orange);margin-top:24px}
.divider{top:28px;width:1px;height:62px;background:var(--navy)}
.social{width:44px;height:44px;border-radius:50%;border:2px solid var(--dark);display:flex;align-items:center;justify-content:center;font-size:12px;font-weight:700;color:var(--dark)}
.social.accent{border-color:var(--orange);color:var(--orange)}

/* nav */
.nav{left:44px;top:133px;width:1102px;height:69px;background:var(--navy);z-index:2;display:flex;align-items:center;padding-left:14px}
.nav a{color:var(--white);font-family:"Roboto",sans-serif;font-size:15px;padding:0 20px;height:46px;display:flex;align-items:center;margin-right:18px}
.nav a.active{background:var(--orange)}
.nav .cta{position:absolute;right:16px;top:12px;background:var(--orange);margin:0}

/* hero */
.hero-panel{top:165px;height:345px}

/* welcome */
.welcome-title{left:58px;top:562px;font-family:"Roboto",sans-serif;font-weight:500;font-size:24px;color:var(--navy)}
.welcome-text{left:58px;top:612px;width:455px;font-size:15px;line-height:22.5px}
.welcome-text p+p{margin-top:18px}
.btn{background:var(--orange);color:var(--white);font-weight:700;font-size:15px;display:flex;align-items:center;justify-content:center}
.collage div{position:absolute}

/* services */
.services{left:0;top:1026px;width:1200px;height:615px;background:var(--light)}
.section-title{font-family:"Roboto",sans-serif;font-size:34px;color:var(--dark);text-align:center;width:1200px;left:0;top:1072px}
.services-intro{left:44px;top:1133px;width:1100px;font-size:15px;line-height:22.5px}
.card-title{font-family:"Roboto",sans-serif;font-size:23px;color:var(--dark)}
.card-text{width:235px;font-size:15px;line-height:22.4px}

/* testimonials */
.testimonials{left:0;top:1698px;width:1200px;height:580px;background:linear-gradient(135deg,#f37232,#ee6a2c 50%,#f27a3f)}
.t-kicker{left:55px;top:1738px;font-size:23px;color:var(--white)}
.t-heading{left:55px;top:1792px;font-family:"Roboto",sans-serif;font-weight:700;font-size:37px;color:var(--white);letter-spacing:.5px}
.t-photo{width:167px;height:96px;border:3px solid var(--white);border-radius:3px}
.t-name{font-size:17px;font-weight:700;color:var(--white);text-align:center;width:300px}
.t-role{font-size:13px;color:var(--white);text-align:center;width:300px}
.t-quote{width:500px;font-size:13.5px;line-height:26px;color:var(--white);text-align:center}
.dot{width:13px;height:13px;border:2px solid var(--white);top:2214px}
.dot.on{background:var(--white)}

/* footer */
.footer{left:0;top:2333px;width:1200px;height:303px;background:linear-gradient(#ffffff,#ececec);border-top:1px solid #eee}
.f-title{font-size:19px;font-weight:700;color:var(--dark)}
.f-input{left:59px;top:2424px;width:316px;height:50px;border:1px solid #cfcfcf;background:var(--white)}
.f-btn{left:59px;top:2491px;width:316px;height:48px;background:var(--orange);color:var(--white);font-family:"Roboto",sans-serif;font-size:22px;display:flex;align-items:center;justify-content:center}
.f-link{font-size:15px;font-weight:700;color:var(--dark)}
.copyright{left:59px;top:2653px;font-size:13px;color:var(--dark)}
</style>
</head>
<body>

<header>
  <div class="abs brand"><span class="brand-dot"></span><span class="brand-name">Brightwire Electrical</span></div>
  <div class="abs contact-block" style="left:614px"><div class="contact-label">CALL US</div><div class="contact-value">+91 900 000 1234</div></div>
  <div class="abs divider" style="left:748px"></div>
  <div class="abs contact-block" style="left:772px"><div class="contact-label">EMAIL US</div><div class="contact-value">hello@brightwire.example</div></div>
  <div class="abs divider" style="left:934px"></div>
  <a class="abs social accent" style="left:957px;top:40px" aria-label="friendspace">fs</a>
  <a class="abs social" style="left:1018px;top:40px" aria-label="snapgram">sg</a>
  <a class="abs social" style="left:1078px;top:40px" aria-label="chirpnet">cn</a>
</header>

<nav class="abs nav">
  <a class="active" href="#">HOME</a>
  <a href="#">MEET THE TEAM</a>
  <a href="#">OUR SERVICES</a>
  <a href="#">OUR PROJECTS</a>
  <a href="#">CONTACT US</a>
  <a class="cta" href="#">MAKE AN APPOINTMENT</a>
</nav>

<section>
  <div class="abs hero-panel" style="left:0;width:290px;background:linear-gradient(160deg,#e9d9c2,#b89575)" role="img" aria-label="Hotel bedroom with warm wall lights"></div>
  <div class="abs hero-panel" style="left:292px;width:543px;background:linear-gradient(160deg,#f2e4d0,#9a6a4c)" role="img" aria-label="Classic bedroom with chandelier and curtains"></div>
  <div class="abs hero-panel" style="left:838px;width:362px;background:linear-gradient(160deg,#eeeeea,#c8c6bd)" role="img" aria-label="Conference room with ceiling lighting"></div>
</section>

<section>
  <h1 class="abs welcome-title">Welcome to Brightwire Electrical</h1>
  <div class="abs welcome-text">
    <p>Welcome test will go here. Welcome test will go here. elcome test ill go here. Welcome test will go here. Welcome test will go here. come test will go here. Welcome test will go ere. Welcome test will gohere. Welcome test will go here.</p>
    <p>Welcome test will go here. Welcome test will go here. elcome tet will go here. Welcome test will go here. Welcome test will go here. come test will go here. Welcome test will go ere. Welcome test will gohere. Welcome test will go here. elcome test will go here. Welcome test e. Welcome test will go here. Welcome test will go here. Welcome test will go here. Welcome test will go here. lcomet will go here.</p>
  </div>
  <a class="abs btn" style="left:56px;top:890px;width:197px;height:43px" href="#">ABOUT OUR MISSION</a>
  <div class="collage">
    <div style="left:552px;top:568px;width:379px;height:262px;background:linear-gradient(150deg,#dfe3de,#b7774e)" role="img" aria-label="Kitchen with pendant lights"></div>
    <div style="left:933px;top:568px;width:213px;height:165px;background:linear-gradient(150deg,#f6ede4,#d8c2a8)" role="img" aria-label="Bright living room with lamp"></div>
    <div style="left:933px;top:735px;width:213px;height:221px;background:linear-gradient(150deg,#efe3cf,#7a3a30)" role="img" aria-label="Bedroom with ceiling light"></div>
    <div style="left:552px;top:832px;width:260px;height:124px;background:linear-gradient(150deg,#f1f1ee,#c9c5b8)" role="img" aria-label="White kitchen with downlights"></div>
    <div style="left:815px;top:832px;width:116px;height:124px;background:linear-gradient(150deg,#a86a3e,#e9e2d6)" role="img" aria-label="Bedroom corner with dresser"></div>
  </div>
</section>

<section>
  <div class="abs services"></div>
  <h2 class="abs section-title">OUR SERVICES</h2>
  <p class="abs services-intro">Our Services text will go here. Our Services text will go here. Our Services text will go here. Our Services text will go here. Our Services text will go here. Our Services text will go here. Our Services text will go here. Our Services text will go here. Our Services text will go here. Our Services text will go here. Our Services text will go here.</p>

  <div class="abs" style="left:47px;top:1222px;width:240px;height:275px;background:linear-gradient(150deg,#efe6da,#8c9ab0)" role="img" aria-label="Home owner relaxing in a bright living room"></div>
  <h3 class="abs card-title" style="left:325px;top:1216px">HOME OWNERS</h3>
  <p class="abs card-text" style="left:326px;top:1268px">Our Services text will go here. ur Services text will go here. Our es text will go here. Our Services xt will go here. Our Services text will go here. Our Services text will go here. Our Services text will go re. Our Services text will go here. ur Services text will go here. Our ces text will go here. Our Services ext will go here.</p>
  <a class="abs btn" style="left:47px;top:1540px;width:132px;height:43px" href="#">MORE INFO</a>

  <div class="abs" style="left:623px;top:1222px;width:240px;height:275px;background:linear-gradient(150deg,#e4e4e2,#8fa44a)" role="img" aria-label="Office space with pendant lamp"></div>
  <h3 class="abs card-title" style="left:901px;top:1216px">BUSINESS OWNERS</h3>
  <p class="abs card-text" style="left:903px;top:1268px">Our Services text will go here. ur Services text will go here. Our es text will go here. Our Services xt will go here. Our Services text will go here. Our Services text will go here. Our Services text will go re. Our Services text will go here. ur Services text will go here. Our ces text will go here. Our Services ext will go here.</p>
  <a class="abs btn" style="left:623px;top:1540px;width:132px;height:43px" href="#">MORE INFO</a>
</section>

<section>
  <div class="abs testimonials"></div>
  <div class="abs t-kicker">Testimonials</div>
  <h2 class="abs t-heading">What our clients say about us...</h2>

  <div class="abs t-photo" style="left:224px;top:1877px;background:linear-gradient(150deg,#dfe6e9,#9db0b8)" role="img" aria-label="Portrait of client Marco Delling"></div>
  <div class="abs t-name" style="left:155px;top:2004px">Marco Delling</div>
  <div class="abs t-role" style="left:153px;top:2030px">Business Person</div>
  <p class="abs t-quote" style="left:55px;top:2117px">We are looking for a website which shows a simple, clear, to the point and trust worthy service. We offer Electrical Services !</p>

  <div class="abs t-photo" style="left:802px;top:1877px;background:linear-gradient(150deg,#eef0f2,#b9c3cc)" role="img" aria-label="Portrait of client Priya Vance"></div>
  <div class="abs t-name" style="left:735px;top:2004px">Priya Vance</div>
  <div class="abs t-role" style="left:738px;top:2030px">Business Women</div>
  <p class="abs t-quote" style="left:635px;top:2117px">We are looking for a website which shows a simple, clear, to the point and trust worthy service. We offer Electrical Services !</p>

  <span class="abs dot" style="left:570px"></span>
  <span class="abs dot" style="left:589px"></span>
  <span class="abs dot on" style="left:608px"></span>
</section>

<footer>
  <div class="abs footer"></div>
  <div class="abs f-title" style="left:62px;top:2383px">Signup for Special deals!</div>
  <div class="abs f-input"></div>
  <a class="abs f-btn" href="#">SUBSCRIBE</a>

  <div class="abs f-title" style="left:688px;top:2383px">Links</div>
  <a class="abs f-link" style="left:688px;top:2429px">Meet The Team</a>
  <a class="abs f-link" style="left:688px;top:2472px">Our Services</a>
  <a class="abs f-link" style="left:688px;top:2515px">Our Products</a>
  <a class="abs f-link" style="left:688px;top:2558px">Contacts</a>

  <div class="abs f-title" style="left:856px;top:2383px">INFO</div>
  <a class="abs f-link" style="left:856px;top:2429px">Privacy Policy</a>
  <a class="abs f-link" style="left:856px;top:2461px">Terms &amp; Conditions</a>
  <a class="abs f-link" style="left:856px;top:2492px">Returns</a>
  <a class="abs f-link" style="left:856px;top:2523px">Customer Service</a>

  <a class="abs social accent" style="left:1056px;top:2387px" aria-label="friendspace">fs</a>
  <a class="abs social" style="left:1056px;top:2446px" aria-label="snapgram">sg</a>
  <a class="abs social" style="left:1056px;top:2504px" aria-label="chirpnet">cn</a>

  <div class="abs copyright">Copyright © 2019 BrightwireElectrical.example all rights reserved.</div>
</footer>

</body>
</html>
```